Modern Academic Informational Postcard and Graphic

I am looking for a postcard design, with a fast turnaround time (24-hours). These postcards will be handed out at a presentation that is being given as part of an interview process. I would like to print two information cards per 8.5/11 piece of paper. These cards will be double sided. The front side is a visual graphic representing the 4 elements of the vision this interview candidate plans to bring to the position. The backside includes a snapshot of this candidate’s academic and administrative background. I have attached a sketch of the front and back sides. There should also be a simple visual on the backside denoting a spot reserved for Marlow Crest College (MC) on this career continuum (on the sketch this is represented by a star with MC in the middle).

I would like the crimson palatte to be used (https://www.marlowcrest-example.edu/brand/design/color.html) and, if possible Benton Sans font. And the overall aesthetic should be modern and minimalistic, and convey professionalism. The information does not have to be presented in the way that it is in the attached documents (this was just a rough sketch/idea).

```html
<!DOCTYPE html>
<html lang="en">
<head>
<meta charset="utf-8">
<title>Inspire Impact – Candidate Postcard</title>
<link rel="stylesheet" href="https://fonts.googleapis.com/css2?family=Oswald:wght@600;700&family=Montserrat:wght@400;500;600&display=swap">
<style>
  :root{
    --crimson:#b00000;
    --ink:#222222;
    --paper:#ffffff;
    --cell:#efefef;
    --rule:#8a8a8a;
    --backdrop:#3a3a3a;
    --charcoal:#1e1e1e;
  }
  *{box-sizing:border-box;margin:0;padding:0}
  html,body{width:1200px;height:1200px;overflow:hidden}
  body{background:var(--backdrop);position:relative;font-family:"Montserrat",sans-serif;color:var(--ink)}
  .card{position:absolute;left:214px;width:773px;height:494px;background:var(--paper);overflow:hidden}
  .card--front{top:77px}
  .card--back{top:629px}
  .card svg.art{position:absolute;inset:0}
  .pillar-label{position:absolute;font-family:"Oswald",sans-serif;font-weight:700;font-size:25px;line-height:26px;color:var(--ink);text-transform:uppercase;letter-spacing:-0.2px}
  .pillar-label--center{text-align:center;transform:translateX(-50%)}

  .band{position:absolute;left:0;top:58px;width:652px;height:34px;background:var(--crimson);color:#fff;
        font-family:"Oswald",sans-serif;font-weight:700;font-size:23px;letter-spacing:2px;text-align:center;line-height:34px;padding-left:40px}
  .wordmark{position:absolute;left:652px;top:38px;width:110px;text-align:center;font-family:"Oswald",sans-serif;font-weight:700;font-size:58px;color:var(--crimson);line-height:90px}
  .candidate{position:absolute;left:0;width:652px;top:106px;text-align:center;font-size:22px;font-weight:500;letter-spacing:1.5px}
  .timeline{position:absolute;top:178px;display:grid;border:1px solid var(--rule);background:var(--paper)}
  .timeline--education{left:15px;width:261px;grid-template-columns:113px 1fr}
  .timeline--university{left:325px;width:434px;grid-template-columns:158px 142px 1fr}
  .timeline div{font-size:12px;line-height:14px;text-align:center;display:flex;align-items:center;justify-content:center;padding:0 2px;white-space:nowrap}
  .role{height:37px;background:var(--crimson);color:#fff;font-weight:600;font-size:11px !important;letter-spacing:0.6px;line-height:13px !important;border-left:1px solid var(--rule)}
  .unit{height:62px;background:var(--cell);border-left:1px solid var(--rule)}
  .place{height:86px;background:var(--paper);border-left:1px solid var(--rule)}
  .timeline .first{border-left:none}
  .sector{grid-column:1/-1;height:30px;background:var(--cell)}
  .placeholder-spot{position:absolute;left:272px;top:342px;width:58px;height:58px;border-radius:50%;background:var(--crimson);border:2px solid #fff;
        color:#fff;font-family:"Oswald",sans-serif;font-weight:700;font-size:24px;display:flex;align-items:center;justify-content:center}
  .contact{position:absolute;left:374px;right:0;top:462px;height:32px;color:#fff;font-size:19px;letter-spacing:1.5px;text-align:center;line-height:32px;padding-left:30px;white-space:nowrap}
</style>
</head>
<body>

<section class="card card--front" aria-label="Vision: Inspire Impact">
  <svg class="art" width="773" height="494" viewBox="0 0 773 494">
    <polygon points="0,0 428,0 418,8 0,8" fill="var(--crimson)"/>
    <polygon points="0,494 0,440 60,370 160,370 90,494" fill="#f2f2f2"/>
    <polygon points="570,494 650,390 760,390 680,494" fill="#f4f4f4"/>
    <polygon points="365,486 773,486 773,494 356,494" fill="var(--crimson)"/>
    <g stroke="var(--crimson)" stroke-width="1.6" fill="var(--crimson)">
      <line x1="33" y1="140" x2="210" y2="140"/><circle cx="33" cy="140" r="3"/>
      <line x1="560" y1="140" x2="742" y2="140"/><circle cx="742" cy="140" r="3"/>
      <line x1="21" y1="377" x2="230" y2="377"/><circle cx="21" cy="377" r="3"/>
      <line x1="534" y1="389" x2="742" y2="389"/><circle cx="742" cy="389" r="3"/>
    </g>
    <circle cx="385" cy="246" r="208" fill="var(--crimson)"/>
    <g stroke="#fff" stroke-width="2.5">
      <line x1="385" y1="42" x2="385" y2="144"/><line x1="385" y1="348" x2="385" y2="450"/>
      <line x1="181" y1="246" x2="283" y2="246"/><line x1="487" y1="246" x2="589" y2="246"/>
    </g>
    <circle cx="385" cy="246" r="102" fill="var(--crimson)" stroke="#fff" stroke-width="2.5"/>
    <text x="385" y="257" text-anchor="middle" font-family="Oswald, sans-serif" font-weight="700" font-size="27" fill="#fff">INSPIRE IMPACT</text>
    <g fill="none" stroke="#fff" stroke-width="2">
      <circle cx="273" cy="142" r="35"/><circle cx="487" cy="142" r="35"/>
      <circle cx="270" cy="351" r="35"/><circle cx="494" cy="351" r="35"/>
      <polygon points="273,126 293,135 273,144 253,135"/>
      <path d="M262,140 v10 q11,7 22,0 v-10"/><line x1="293" y1="135" x2="293" y2="148"/>
      <rect x="474" y="124" width="26" height="34" rx="2"/><rect x="481" y="120" width="12" height="6"/>
      <path d="M478,133 l2,2 4,-4 M478,142 l2,2 4,-4 M478,151 l2,2 4,-4"/>
      <path d="M487,133 h9 M487,142 h9 M487,151 h9"/>
      <circle cx="270" cy="351" r="9"/>
      <path d="M270,342 v-9 M270,360 v9 M261,351 h-9 M279,351 h9 M264,345 l-7,-7 M276,345 l7,-7 M264,357 l-7,7 M276,357 l7,7"/>
      <circle cx="270" cy="331" r="2.5"/><circle cx="270" cy="371" r="2.5"/><circle cx="250" cy="351" r="2.5"/><circle cx="290" cy="351" r="2.5"/>
      <path d="M478,336 h32 a4,4 0 0 1 4,4 v18 a4,4 0 0 1 -4,4 h-18 l-8,7 v-7 h-6 a4,4 0 0 1 -4,-4 v-18 a4,4 0 0 1 4,-4z"/>
      <path d="M484,345 h5 l10,-5 v18 l-10,-5 h-5z"/>
    </g>
  </svg>
  <div class="pillar-label pillar-label--center" style="left:118px;top:85px">Student<br>Experiences</div>
  <div class="pillar-label pillar-label--center" style="left:652px;top:85px">Organizational<br>Capacity</div>
  <div class="pillar-label pillar-label--center" style="left:110px;top:320px">Outreach<br>and Leadership</div>
  <div class="pillar-label" style="left:578px;top:320px">Assessment and<br>Communications</div>
</section>

<section class="card card--back" aria-label="Academic and administrative background">
  <svg class="art" width="773" height="494" viewBox="0 0 773 494">
    <polygon points="0,470 0,420 30,392 130,392 40,470" fill="#f2f2f2"/>
    <polygon points="560,462 640,392 740,392 660,462" fill="#f4f4f4"/>
    <polygon points="0,475 378,475 368,494 0,494" fill="var(--charcoal)"/>
    <polygon points="392,462 773,462 773,494 374,494" fill="var(--crimson)"/>
  </svg>
  <div class="band">ACADEMIC AND ADMINISTRATIVE BACKGROUND</div>
  <div class="wordmark">MC</div>
  <div class="candidate">DANA R. WHITFIELD (SHE/HER)</div>

  <div class="timeline timeline--education">
    <div class="role first">TEACHER</div><div class="role">PROFESSOR</div>
    <div class="unit first">Larkin Middle<br>School</div><div class="unit">Educational Leadership<br>&amp; Policy Studies</div>
    <div class="place first">Brookside ISD<br>Houston, Texas<br>1998-2000</div><div class="place">Kestrel University<br>2004 - present</div>
    <div class="sector">Education</div>
  </div>

  <div class="timeline timeline--university">
    <div class="role first">DIRECTOR OF<br>ACADEMIC INCLUSION</div><div class="role">INTERIM<br>VICE PROVOST</div><div class="role">ASSOCIATE<br>VICE PROVOST</div>
    <div class="unit first">Office of<br>Diversity &amp; Equity</div><div class="unit">Office of<br>Diversity &amp; Equity</div><div class="unit">Office of<br>Faculty Affairs</div>
    <div class="place first">Kestrel University<br>2018-2019</div><div class="place">Kestrel University<br>2019-2021</div><div class="place">Kestrel University<br>2021-2023</div>
    <div class="sector">University</div>
  </div>

  <div class="placeholder-spot">MC</div>
  <div class="contact">DRW@KESTRELU.EDU</div>
</section>

</body>
</html>
```